Logo & Responsive Website Design for Mortgage Company

Talvo Mortgage is a new Mortgage Fin-Tech company that will use its own innovative, proprietary technology for lead generation, mortgage origination, and processing of residential home loans in the US. The design should convey that we are a technology-driven company, offering borrowers seeking home loans an exceptional experience throughout the borrowing process.

We are looking for designs that are elegant, convey technical competency, simple to navigate, and set us apart from the competition.

We are not set on any particular colors at this point, so feel free to choose the best colors for your particular designs.

Please include both desktop and mobile designs.

Some Examples of Mortgage Websites. These are to show the typical content, not designs that we particularly like or dislike.
https://www.pondrel.example/
https://www.kmtfunding.example/
https://dulvamortgage.example/
https://wexo.example/
https://primecoastlending.example/

Please send comments with additional questions.

Thank You For your participation.

Target Market(s)

U.S. Residential Home Loan Seekers

Industry/Entity Type

FinTech Mortgage

Number of Pages Required

2 page

```html
<!DOCTYPE html>
<html lang="en">
<head>
<meta charset="utf-8">
<title>Talvo Mortgage</title>
<link href="https://fonts.googleapis.com/css2?family=Poppins:wght@400;500;600;700&display=swap" rel="stylesheet">
<style>
:root{
  --blue:#1b6fc6;
  --blue-dark:#1766b8;
  --blue-light:#bfe3f5;
  --sky:#e4f5fb;
  --orange:#f7941d;
  --green:#17862e;
  --ink:#333333;
  --text:#555555;
  --footer:#333333;
  --white:#ffffff;
}
*{box-sizing:border-box;margin:0;padding:0}
html,body{width:1200px;height:4090px;overflow:hidden;background:var(--white)}
body{font-family:"Poppins",sans-serif;color:var(--ink);position:relative}
.abs{position:absolute}
a{color:inherit;text-decoration:none}

/* header */
.site-header{position:absolute;top:0;left:0;width:1200px;height:87px;background:var(--white)}
.brand{position:absolute;left:144px;top:18px;font-weight:700;font-size:30px;color:var(--blue);letter-spacing:1px;line-height:1}
.brand small{display:block;font-size:13px;color:var(--ink);font-weight:600;letter-spacing:1.5px;text-align:right;margin-top:2px}
.nav{position:absolute;left:406px;top:38px;display:flex;gap:27px;font-size:13px;color:var(--ink)}
.btn{display:inline-flex;align-items:center;justify-content:center;border-radius:40px;font-weight:600}
.btn-orange{background:var(--orange);color:var(--white)}
.btn-outline{border:2px solid var(--blue);color:var(--blue);background:var(--white)}
.btn-green{background:var(--green);color:var(--white)}

/* hero */
.hero{position:absolute;top:87px;left:0;width:1200px;height:650px;background:linear-gradient(180deg,#bfe6f4 0%,#e7f6fb 70%,#f3fbfe 100%);overflow:hidden}
.hero h1{position:absolute;left:144px;top:180px;font-size:38px;line-height:44px;color:var(--blue);font-weight:700}
.hero p{position:absolute;left:144px;top:276px;font-size:17px;line-height:30px;color:var(--ink)}
.hero-art{position:absolute;left:508px;top:100px;width:667px;height:420px;border-radius:24px;background:radial-gradient(circle at 55% 45%,#f9c77c 0%,#8fcde4 45%,rgba(191,230,244,0) 75%)}

/* section titles */
.section-title{position:absolute;left:0;width:1200px;text-align:center;font-size:35px;font-weight:600;color:var(--ink)}
.section-title span{color:var(--blue)}
.rule{position:absolute;height:2px;background:var(--blue)}

/* steps */
.step{position:absolute;width:300px;text-align:center}
.step-icon{width:100px;height:100px;margin:0 auto 24px;border-radius:20px;background:linear-gradient(135deg,#d6eafa,#fde4c3)}
.step h3{font-size:19px;color:var(--blue);font-weight:600;margin-bottom:6px}
.step p{font-size:14.5px;line-height:26px;color:var(--text)}

/* family */
.family{position:absolute;top:1224px;left:0;width:1200px;height:455px;background:#f4f4f4;overflow:hidden}
.family-photo{position:absolute;left:524px;top:0;width:676px;height:455px;background:linear-gradient(90deg,#f4f4f4 0%,#e3ddd6 25%,#c9ab8c 60%,#9c8a7a 100%)}
.family h2{position:absolute;left:144px;top:82px;font-size:37px;line-height:45px;font-weight:600;color:var(--ink)}
.family h2 span{color:var(--blue)}
.family p{position:absolute;left:144px;top:222px;font-size:14.5px;line-height:26px;color:var(--text)}

/* partners */
.partners{position:absolute;top:1850px;left:144px;width:912px;display:flex;justify-content:space-between;align-items:center;font-weight:700}
.dots{position:absolute;top:1936px;left:568px;display:flex;gap:10px}
.dots i{width:9px;height:9px;border-radius:50%;background:#777}
.dots i:first-child{background:var(--blue)}

/* rates */
.rates-card{position:absolute;left:376px;top:2236px;width:346px;height:335px;background:var(--white);border-radius:8px;box-shadow:0 6px 20px rgba(0,0,0,.15);text-align:center}
.rates-card .label{margin-top:100px;font-size:15px;font-weight:500;color:var(--ink)}
.rates-card .rate{font-size:66px;font-weight:700;color:var(--green);line-height:1.2;margin-top:6px}
.rates-card .apr{font-size:14px;color:var(--ink)}
.rates-card .apr a{color:var(--blue)}
.lender{position:absolute;width:220px;left:140px;text-align:center;color:var(--white);font-weight:700}
.rates-title{position:absolute;left:751px;top:2272px;font-size:36px;line-height:45px;font-weight:700;color:var(--white)}
.rates-text{position:absolute;left:751px;top:2412px;font-size:14.5px;line-height:28px;color:var(--white)}

/* reviews */
.reviews-title{position:absolute;left:144px;top:2790px;font-size:36px;font-weight:600;color:var(--ink)}
.reviews-title span{color:var(--blue)}
.score{position:absolute;left:660px;top:2770px;width:160px;text-align:center}
.score b{display:block;font-size:66px;line-height:1;color:var(--blue);font-weight:700}
.score small{display:block;font-size:14px;line-height:21px;color:var(--ink);margin-top:4px}
.verified{position:absolute;left:840px;top:2768px;width:220px;text-align:center}
.verified .vname{font-size:34px;font-weight:500;color:var(--blue);line-height:1.1}
.verified .vsub{font-size:24px;color:var(--ink);line-height:1.3}
.stars{color:var(--orange);letter-spacing:3px}
.review{position:absolute;top:2925px;width:290px}
.review .stars{font-size:17px}
.review h4{font-size:21px;font-weight:500;color:var(--ink);margin:4px 0 10px}
.review p{font-size:13px;line-height:24px;color:var(--text)}
.review .who{margin-top:18px;font-size:12.5px;line-height:25px;color:var(--ink)}
.review .who b{color:var(--blue);font-weight:600}
.arrow{position:absolute;top:3030px}

/* cta */
.cta-title{position:absolute;left:0;width:1200px;top:3522px;text-align:center;font-size:37px;font-weight:700;color:var(--white)}
.cta-text{position:absolute;left:0;width:1200px;top:3612px;text-align:center;font-size:16.5px;line-height:27px;color:var(--white)}

/* footer */
.site-footer{position:absolute;top:3801px;left:0;width:1200px;height:289px;background:var(--footer);color:var(--white)}
.foot-brand{position:absolute;left:144px;top:80px;font-weight:700;font-size:32px;letter-spacing:1px;line-height:1}
.foot-brand small{display:block;font-size:13px;font-weight:600;letter-spacing:1.5px;text-align:right;margin-top:2px}
.foot-copy{position:absolute;left:144px;top:174px;font-size:12px;line-height:25px}
.foot-col{position:absolute;top:74px;font-size:13px;line-height:36px}
.foot-social{position:absolute;left:795px;top:74px;width:260px;font-size:12.5px;line-height:21px}
.social{display:flex;gap:8px;margin-top:18px}
.social i{width:27px;height:27px;border:1.5px solid var(--white);border-radius:50%}
</style>
</head>
<body>

<header class="site-header">
  <div class="brand">TALVO<small>MORTGAGE</small></div>
  <nav class="nav"><a>How it Works</a><a>Today's Rates</a><a>About Us</a><a>Reviews</a></nav>
  <a class="btn btn-orange abs" style="left:803px;top:25px;width:137px;height:40px;font-size:14px">Get Started</a>
  <a class="btn btn-outline abs" style="left:950px;top:25px;width:106px;height:40px;font-size:14px">Sign In</a>
</header>

<section class="hero">
  <h1>Get a Great<br>Mortgage Rate</h1>
  <p>Nemo enim ipsam voluptatem quia<br>voluptas sit aspernatur aut odit<br>aut fugit, sed quia consequuntur magni</p>
  <a class="btn btn-green abs" style="left:144px;top:381px;width:184px;height:48px;font-size:15px">I'm purchasing</a>
  <a class="btn btn-green abs" style="left:338px;top:381px;width:182px;height:48px;font-size:15px">I'm purchasing</a>
  <div class="hero-art" role="img" aria-label="Illustration of a house, a large calculator, coins, charts and two people reviewing mortgage figures"></div>
  <svg class="abs" style="left:0;top:490px" width="1200" height="160" viewBox="0 0 1200 160" preserveAspectRatio="none">
    <path d="M0 80 C150 40 260 150 420 90 C560 40 700 140 860 80 C1000 30 1100 90 1200 60 L1200 160 L0 160Z" fill="#a9d9f1" opacity=".6"/>
    <path d="M0 155 C80 120 140 100 220 120 C330 150 420 90 560 110 C700 130 820 70 960 100 C1080 125 1140 110 1200 120 L1200 160 L0 160Z" fill="#ffffff"/>
  </svg>
</section>

<h2 class="section-title" style="top:800px">How <span>Talvo Mortgage</span> Works</h2>
<div class="rule" style="left:528px;top:868px;width:144px"></div>

<div class="step" style="left:137px;top:916px">
  <div class="step-icon" role="img" aria-label="Line icon of two people talking across a table"></div>
  <h3>Inquire Now</h3>
  <p>Sed ut perspiciatis unde omnis<br>iste natus error sit voluptatem ac<br>cusantium dolorem</p>
</div>
<div class="step" style="left:448px;top:916px">
  <div class="step-icon" role="img" aria-label="Line icon of a hand choosing between options"></div>
  <h3>Learn About Your Options</h3>
  <p>Sed ut perspiciatis unde omnis<br>iste natus error sit voluptatem ac<br>cusantium dolorem</p>
</div>
<div class="step" style="left:764px;top:916px">
  <div class="step-icon" role="img" aria-label="Line icon of an approved document with a stamp"></div>
  <h3>Get Approved and Close</h3>
  <p>Sed ut perspiciatis unde omnis<br>iste natus error sit voluptatem ac<br>cusantium dolorem</p>
</div>

<section class="family">
  <div class="family-photo" role="img" aria-label="Photo of a smiling family sitting on moving boxes in their new home"></div>
  <h2>Everything you need,<br><span>all in one place.</span></h2>
  <p>Sed ut perspiciatis unde omnis iste natus error sit voluptatem<br>accusantium doloremque laudantium inventore veritatis<br>et quasi architecto beatae vitae dicta sunt explicabo</p>
  <a class="btn btn-orange abs" style="left:144px;top:320px;width:176px;height:40px;font-size:14px">Get Started</a>
</section>

<h2 class="section-title" style="top:1736px">Our Trusted <span>Partners</span></h2>
<div class="rule" style="left:528px;top:1806px;width:144px;background:#cccccc"></div>
<div class="partners">
  <span style="color:var(--blue);font-size:22px">Corvane Lending</span>
  <span style="color:#1c2a52;font-size:26px">harbornest</span>
  <span style="color:#c8102e;font-size:22px">Brightmast Bank</span>
  <span style="color:#2a4a7a;font-size:18px">Ostrel Home Loans</span>
</div>
<div class="dots"><i></i><i></i><i></i><i></i></div>

<svg class="abs" style="left:0;top:2010px" width="1200" height="700" viewBox="0 0 1200 700" preserveAspectRatio="none">
  <defs><linearGradient id="rateBand" x1="0" x2="1"><stop offset="0" stop-color="#1b6fc6"/><stop offset="1" stop-color="#2b8fd6"/></linearGradient></defs>
  <path d="M0 100 C200 60 380 150 560 90 C740 20 900 0 1050 30 C1120 45 1170 70 1200 90 L1200 300 L0 300Z" fill="#cfeaf8"/>
  <path d="M0 130 C220 140 400 60 600 70 C800 80 950 40 1200 110 L1200 680 L0 680Z" fill="url(#rateBand)"/>
  <path d="M0 620 C160 580 300 660 480 630 C650 600 780 560 950 610 C1060 640 1140 600 1200 620 L1200 700 L0 700Z" fill="#6fb8e8" opacity=".7"/>
  <path d="M0 690 C200 640 380 700 560 660 C760 620 900 690 1080 650 C1140 640 1180 650 1200 660 L1200 700 L0 700Z" fill="#ffffff"/>
</svg>

<div class="lender" style="top:2262px;font-size:20px">VELTRA MORTGAGE</div>
<div class="lender" style="top:2338px;font-size:22px">QUILLON<br><span style="font-size:15px;font-weight:400">Mortgage</span></div>
<div class="lender" style="top:2428px;font-size:22px;letter-spacing:1px">MARLOW<br><span style="font-size:10px;font-weight:400;letter-spacing:2px">MORTGAGE CORPORATION</span></div>
<div class="lender" style="top:2510px;font-size:22px">FENWICK HOME</div>

<div class="rates-card">
  <div class="label">15 YEAR FIXED</div>
  <div class="rate">4.98%*</div>
  <div class="apr">* 4.192% APR, see <a>rate assumptions</a></div>
</div>
<h2 class="rates-title">Today's<br>Mortgage Rates</h2>
<div class="rule" style="left:751px;top:2378px;width:150px;background:var(--white)"></div>
<p class="rates-text">Nemo enim ipsam voluptatem quia<br>voluptas sit &nbsp;aspernatur aut odit aut<br>fugit, sed quia consequuntur magni<br>dolores eos qui ratio</p>

<h2 class="reviews-title">What People <span>Are Saying</span></h2>
<div class="rule" style="left:144px;top:2855px;width:102px;background:#cccccc"></div>
<div class="score"><b>4.98</b><small>427 verified<br>customer reviews</small></div>
<div class="verified">
  <div class="vname">Trustline</div>
  <div class="vsub">Verified Reviews</div>
  <div style="display:flex;justify-content:center;align-items:center;gap:6px;margin-top:2px">
    <svg width="22" height="22" viewBox="0 0 22 22"><circle cx="11" cy="11" r="10" fill="var(--green)"/><path d="M6 11l3.5 3.5L16 8" stroke="#fff" stroke-width="2.5" fill="none"/></svg>
    <span class="stars" style="font-size:24px">★★★★★</span>
  </div>
</div>

<svg class="arrow" style="left:107px" width="24" height="22" viewBox="0 0 24 22"><path d="M22 11H3M11 3L3 11l8 8" stroke="#333" stroke-width="2.6" fill="none"/></svg>
<svg class="arrow" style="left:1066px" width="24" height="22" viewBox="0 0 24 22"><path d="M2 11h19M13 3l8 8-8 8" stroke="#333" stroke-width="2.6" fill="none"/></svg>

<article class="review" style="left:144px">
  <div class="stars">★★★★★</div>
  <h4>Neque porro quisquam</h4>
  <p>Nemo enim ipsam voluptatem quia voluptas sit &nbsp;aspernatur aut odit aut fugit, sed quia consequuntur magni dolores eos qui ratione volupt.</p>
  <div class="who"><b>Marco T.</b> Verified Reviewer<br>Lakeview Hollow, CA (Sep 2022)</div>
</article>
<article class="review" style="left:455px">
  <div class="stars">★★★★★</div>
  <h4>Neque porro quisquam</h4>
  <p>Nemo enim ipsam voluptatem quia voluptas sit &nbsp;aspernatur aut odit aut fugit, sed quia consequuntur magni dolores eos qui ratione volupt.</p>
  <div class="who"><b>Marco T.</b> Verified Reviewer<br>Lakeview Hollow, CA (Sep 2022)</div>
</article>
<article class="review" style="left:770px">
  <div class="stars">★★★★★</div>
  <h4>Neque porro quisquam</h4>
  <p>Nemo enim ipsam voluptatem quia voluptas sit &nbsp;aspernatur aut odit aut fugit, sed quia consequuntur magni dolores eos qui ratione volupt.</p>
  <div class="who"><b>Marco T.</b> Verified Reviewer<br>Lakeview Hollow, CA (Sep 2022)</div>
</article>

<a class="btn btn-outline abs" style="left:501px;top:3218px;width:197px;height:45px;font-size:14px;border-width:1.5px">See all reviews</a>

<svg class="abs" style="left:0;top:3330px" width="1200" height="472" viewBox="0 0 1200 472" preserveAspectRatio="none">
  <path d="M0 70 C200 20 400 110 620 70 C820 30 1000 0 1200 40 L1200 472 L0 472Z" fill="#cfeaf8"/>
  <path d="M0 130 C250 80 450 150 700 110 C900 80 1050 90 1200 120 L1200 472 L0 472Z" fill="#7fc1ea" opacity=".7"/>
  <path d="M0 150 C250 120 480 100 720 130 C920 150 1080 110 1200 130 L1200 472 L0 472Z" fill="#1b6fc6"/>
</svg>
<h2 class="cta-title">Get a Rate Quote in Just 30 Seconds!</h2>
<div class="rule" style="left:526px;top:3593px;width:148px;background:var(--white)"></div>
<p class="cta-text">Mortgage rates change daily and vary depending on your unique situation.<br>Get your FREE customized quote here!</p>
<a class="btn btn-orange abs" style="left:440px;top:3698px;width:320px;height:42px;font-size:14px">Get My Custom Rate Quote Rate Now</a>

<footer class="site-footer">
  <div class="foot-brand">TALVO<small>MORTGAGE</small></div>
  <div class="foot-copy">Copyright © 2022 Talvo Mortgage<br>All Right Reserved</div>
  <div class="foot-col" style="left:416px">How it Works<br>Today's Rates<br>About Us<br>Reviews</div>
  <div class="foot-col" style="left:590px">Terms of Service<br>Privacy Policy<br>FAQ's<br>Log In</div>
  <div class="foot-social">Follow us on all of our social<br>media accounts to stay up to<br>date with the latest mortgage news,<br>tips and updates.
    <div class="social"><i></i><i></i><i></i><i></i></div>
  </div>
</footer>

</body>
</html>
```